" Window Blinds and Shutters Business Card Design"

We require a business card design for a new windows blinds and shutters company based in Sydney.
The business name is 'Harbourlight Blinds and Shutters'.
We supply and install homes and businesses with internal and external window furnishings and finishes. This includes varieties of window blinds and window shutters.

Benefits of Harbourlight Blinds and Shutters :
Added security and privacy,
The ability to control the amount of sunlight,
Regulate internal temperature.

Blinds varieties:
Roller Blinds, Double Roller Blinds, Roman Blinds, Vertical Blinds, Aluminium venetians, Timber venetians and PVC Venetians.

Shutters varieties:
Plantation Shutters, Aluminium Louvre Shutters, Roller Shutters and Security Shutters .

Hi Designers,

Please have a look at my Business card design brief. I need your help to start my new business.

Thanks,

Daniel.

Reason: not 100% happy with the options available, close to 90% happy, need a little more refinement. Thank You & Good Luck

Target Market(s)

Home owners, business owners, shift workers , and new home builders.

Industry/Entity Type

Security

Contact Information for Business Card

Harbourlight Blinds and Shutters,

Daniel Brostow mobile: 0417586204,
Corey Wendt mobile: 0419248653,

email: daniel.brostow@mailvista.net
web: harbourlightblindsandshutters.com.au

Colors
ffffff
9d9d9d
f78f20

Requirements
Must have
• ON FRONT OF CARD
I have attached a picture of logo and need a designer to design a font logo for Harbourlight Blinds and Shutters similar, or open to suggestions.

FRONT OF CARD
Company message/:
"Framing Your Home with Care"

BACK OF CARD
'For a FREE measure & quote call Daniel - 0417586204"
Nice to have
• Elegant yet professional.

Soft colours appealing to both male & female clients.

Should not have

• Unprofessional fonts

```html
<!DOCTYPE html>
<html lang="en">
<head>
<meta charset="utf-8">
<title>Harbourlight Blinds and Shutters – Business Card</title>
<link rel="stylesheet" href="https://fonts.googleapis.com/css2?family=Lato:wght@400;700;900&family=Libre+Baskerville:ital,wght@0,400;1,400&family=Arimo:wght@700&display=swap">
<style>
  :root {
    --brand-red: #e8262b;
    --brand-blue: #1b5aa6;
    --card-white: #ffffff;
    --stage: #e9e9e9;
    --card-shadow: rgba(0, 0, 0, 0.18);
  }
  * { box-sizing: border-box; margin: 0; padding: 0; }
  html, body {
    width: 1200px; height: 1000px; overflow: hidden;
    background: var(--stage);
    font-family: "Lato", sans-serif;
  }
  .card {
    position: absolute; left: 250px;
    width: 700px; height: 400px;
    background: var(--card-white);
    box-shadow: 0 6px 18px var(--card-shadow);
    overflow: hidden;
  }
  .card--front { top: 60px; }
  .card--back { top: 540px; }

  .header-band {
    position: absolute; left: 0; top: 0; width: 100%;
    background: var(--brand-red);
    display: flex; align-items: center;
  }
  .card--front .header-band { height: 130px; padding-left: 60px; }
  .card--back .header-band { height: 108px; padding-left: 160px; }
  .header-rule {
    position: absolute; left: 0; width: 100%; height: 6px;
    background: var(--brand-red);
  }
  .card--front .header-rule { top: 136px; }
  .card--back .header-rule { top: 114px; }

  .brand { display: flex; align-items: center; gap: 18px; }
  .brand__mark {
    width: 64px; height: 64px;
    background: var(--brand-blue);
    border: 3px solid var(--card-white);
    flex: none;
  }
  .brand__name {
    color: var(--card-white);
    font-family: "Lato", sans-serif;
    font-weight: 700;
    font-size: 28px; line-height: 1.1;
    letter-spacing: 0.5px;
  }

  .offer {
    position: absolute; left: 0; top: 168px; width: 100%;
    text-align: center;
  }
  .offer__lead {
    font-family: "Libre Baskerville", serif; font-style: italic;
    color: var(--brand-blue); font-size: 32px;
  }
  .offer__call {
    margin-top: 22px;
    font-family: "Libre Baskerville", serif;
    color: var(--brand-red); font-size: 32px; letter-spacing: 1px;
  }
  .offer__number {
    display: inline-block; margin-top: 8px;
    background: var(--brand-blue); color: var(--card-white);
    font-family: "Arimo", sans-serif; font-weight: 700;
    font-size: 52px; line-height: 1; padding: 8px 24px 10px;
  }

  .partners-title {
    position: absolute; left: 0; top: 140px; width: 100%;
    text-align: center;
    color: var(--brand-red); font-weight: 700; font-size: 24px;
  }
  .partner { position: absolute; color: var(--brand-blue); }
  .partner--primary { left: 40px; top: 186px; }
  .partner--secondary { right: 50px; top: 248px; }
  .partner__name { font-weight: 900; font-size: 26px; margin-bottom: 22px; }
  .partner__line { font-size: 19px; margin-bottom: 8px; }
  .partner__label { font-weight: 700; }

  .footer-web, .footer-tagline {
    position: absolute; bottom: 0; height: 48px;
    display: flex; align-items: center;
    color: var(--card-white); font-weight: 700; font-size: 17px;
    white-space: nowrap;
  }
  .footer-web {
    left: 0; width: 400px; padding-left: 30px;
    background: var(--brand-blue);
    clip-path: polygon(0 0, 100% 0, calc(100% - 22px) 100%, 0 100%);
  }
  .footer-tagline {
    right: 0; width: 300px; justify-content: center; padding-left: 22px;
    background: var(--brand-red);
    clip-path: polygon(22px 0, 100% 0, 100% 100%, 0 100%);
  }
</style>
</head>
<body>

<section class="card card--front" aria-label="Card front">
  <header class="header-band">
    <div class="brand">
      <span class="brand__mark"></span>
      <span class="brand__name">Harbourlight<br>Blinds and Shutters</span>
    </div>
  </header>
  <div class="header-rule"></div>
  <div class="offer">
    <p class="offer__lead">For a Free Measure and Quote!</p>
    <p class="offer__call">CALL US AT</p>
    <p class="offer__number">0417586204</p>
  </div>
</section>

<section class="card card--back" aria-label="Card back">
  <header class="header-band">
    <div class="brand">
      <span class="brand__mark"></span>
      <span class="brand__name">Harbourlight<br>Blinds and Shutters</span>
    </div>
  </header>
  <div class="header-rule"></div>
  <h2 class="partners-title">BUSINESS PARTNERS</h2>
  <div class="partner partner--primary">
    <p class="partner__name">Daniel Brostow</p>
    <p class="partner__line"><span class="partner__label">M:</span> 0417586204</p>
    <p class="partner__line"><span class="partner__label">E:</span> daniel.brostow@mailvista.net</p>
  </div>
  <div class="partner partner--secondary">
    <p class="partner__name">Corey Wendt</p>
    <p class="partner__line"><span class="partner__label">M:</span> 0419248653</p>
  </div>
  <div class="footer-web">www.harbourlightblindsandshutters.com.au</div>
  <div class="footer-tagline">"Framing Your Home with Care"</div>
</section>

</body>
</html>
```